First Aid Training business needs business card design

We would like a double sided business card designed for a first aid training business - Brindlewood First Aid. We provide first aid training and , WHS (work, health and safety) training.

The attached word document contains the key information we would like on each side of the business card.

Final design needs to be delivered in print ready format, along with the original file.

```html
<!DOCTYPE html>
<html lang="en">
<head>
<meta charset="utf-8">
<title>Brindlewood First Aid – Business Card</title>
<link rel="stylesheet" href="https://fonts.googleapis.com/css2?family=Montserrat:wght@700&family=Nunito:wght@400;600&display=swap">
<style>
  :root {
    --backdrop: #e4e4e4;
    --brand-red: #ed1f24;
    --ink: #141414;
    --paper: #ffffff;
    --card-w: 540px;
    --card-h: 309px;
  }
  * { box-sizing: border-box; margin: 0; padding: 0; }
  html, body { width: 1200px; height: 804px; overflow: hidden; }
  body {
    background: var(--backdrop);
    font-family: "Nunito", sans-serif;
    position: relative;
  }
  .card {
    position: absolute;
    top: 247px;
    width: var(--card-w);
    height: var(--card-h);
    border-radius: 14px;
    overflow: hidden;
    box-shadow: 0 6px 18px rgba(0,0,0,.18);
  }
  /* Front */
  .card-front { left: 40px; background: var(--brand-red); }
  .brand-mark {
    position: absolute; left: 50%; top: 38px;
    width: 68px; height: 68px; margin-left: -34px;
    border-radius: 50%; background: var(--paper);
  }
  .brand-name {
    position: absolute; left: 0; right: 0; top: 122px;
    text-align: center;
    font-family: "Montserrat", sans-serif;
    font-weight: 700; font-size: 34px; line-height: 1.08;
    color: var(--ink); letter-spacing: .5px;
  }
  .brand-services {
    position: absolute; left: 0; right: 0; bottom: 30px;
    text-align: center; color: var(--paper);
    font-size: 15px; letter-spacing: 1.5px;
  }
  /* Back */
  .card-back { left: 620px; background: var(--paper); }
  .pitch {
    position: absolute; left: 26px; top: 20px;
    font-size: 19px; line-height: 26px; letter-spacing: 1.6px;
    color: var(--ink);
  }
  .benefits {
    position: absolute; left: 26px; top: 80px;
    list-style: none;
    font-size: 15px; line-height: 22px; letter-spacing: 1.4px;
    color: var(--brand-red);
  }
  .benefits li { position: relative; padding-left: 22px; }
  .benefits .tick { position: absolute; left: 0; top: 5px; width: 15px; height: 12px; }
  .name-band {
    position: absolute; left: 292px; right: 0; top: 126px; height: 16px;
    background: var(--brand-red);
    border-radius: 8px 0 0 8px;
  }
  .name-band-icon { position: absolute; left: 286px; top: 121px; width: 26px; height: 26px; }
  .holder-name {
    position: absolute; left: 324px; top: 146px;
    font-size: 26px; font-weight: 600; letter-spacing: 2.5px;
    color: var(--brand-red);
  }
  .holder-role {
    position: absolute; left: 324px; top: 182px;
    font-size: 15px; letter-spacing: 1.5px; color: var(--ink);
  }
  .contacts {
    position: absolute; left: 282px; top: 214px; list-style: none;
    font-size: 11.5px; letter-spacing: 1.1px; color: var(--ink);
  }
  .contacts li { display: flex; align-items: center; height: 26px; }
  .contacts svg { width: 20px; height: 20px; margin-right: 8px; flex: none; }
</style>
</head>
<body>

<section class="card card-front" aria-label="Business card front">
  <div class="brand-mark"></div>
  <div class="brand-name">BRINDLEWOOD<br>FIRST AID</div>
  <div class="brand-services">First Aid Training | WHS Training</div>
</section>

<section class="card card-back" aria-label="Business card back">
  <p class="pitch">Onsite Training –<br>We can come to you</p>
  <ul class="benefits">
    <li><svg class="tick" viewBox="0 0 15 12"><path d="M1 7l4 4L14 1" fill="none" stroke="#141414" stroke-width="2.6"/></svg>Time efficient</li>
    <li><svg class="tick" viewBox="0 0 15 12"><path d="M1 7l4 4L14 1" fill="none" stroke="#141414" stroke-width="2.6"/></svg>Cost effective</li>
    <li><svg class="tick" viewBox="0 0 15 12"><path d="M1 7l4 4L14 1" fill="none" stroke="#141414" stroke-width="2.6"/></svg>Minimise downtime<br>for your team</li>
  </ul>

  <div class="name-band"></div>
  <svg class="name-band-icon" viewBox="0 0 26 26">
    <circle cx="13" cy="13" r="13" fill="#ed1f24"/>
    <circle cx="13" cy="10" r="4" fill="none" stroke="#fff" stroke-width="1.6"/>
    <path d="M6.5 20c1-4 4-5.5 6.5-5.5s5.5 1.5 6.5 5.5z" fill="none" stroke="#fff" stroke-width="1.6"/>
  </svg>
  <div class="holder-name">Dana Hollis</div>
  <div class="holder-role">Job Title</div>

  <ul class="contacts">
    <li>
      <svg viewBox="0 0 20 20"><circle cx="10" cy="10" r="10" fill="#ed1f24"/><path d="M7 5.5l2 2-1.2 1.4c.7 1.4 1.6 2.3 3 3l1.4-1.2 2 2-1.4 1.6c-3.5-.4-6.8-3.7-7.2-7.2z" fill="#fff"/></svg>
      0455 212 807
    </li>
    <li>
      <svg viewBox="0 0 20 20"><circle cx="10" cy="10" r="10" fill="#ed1f24"/><rect x="5" y="6.5" width="10" height="7" fill="none" stroke="#fff" stroke-width="1.3"/><path d="M5 6.5l5 4 5-4" fill="none" stroke="#fff" stroke-width="1.3"/></svg>
      help@brindlewoodfirstaid.com.au
    </li>
    <li>
      <svg viewBox="0 0 20 20"><circle cx="10" cy="10" r="10" fill="#ed1f24"/><g fill="none" stroke="#fff" stroke-width="1.2"><circle cx="10" cy="10" r="5"/><ellipse cx="10" cy="10" rx="2.2" ry="5"/><path d="M5 10h10"/></g></svg>
      www.brindlewoodfirstaid.com.au
    </li>
  </ul>
</section>

</body>
</html>
```